Quorvane Website re-design with new logo and look

Refresh on current website. Incorporate new logo which is attached. We provide technology SAAS services to the healthcare space. Current website is at quorvane.com but the new name is Quorvane.com (see logo) Key considerations are as follows:
1. Incorporate a promo video location. I have a new video coming out similar to this one. https://www.plinthery.net/gallery/41730562/Mobile-Application-Promo
2. Incorporate platform features section. as an example see this website where it has mini screens that call out various features ie; "all in one GCR platform" see webiste https://www.dovemk.io/
3. Add some color splash from the log throughout the website
4. Where possible use the text from our website Quorvane.com where not possible use lorem ipsum and we will complete
5. use current theme colors
6. Please use your skills to make it more functional and useful and not replicate what we have.

Target Market(s)

Imaging centers and hospitals

Industry/Entity Type

Healthcare

Coding

Coded - Design and coding required

Number of Pages Required

5+ page

Font styles to use
Sans Serif

Requirements
Must have
• Note section in this website that shows features of the platform as you scoll down. See website https://www.dovemk.io/
Nice to have
• Professional look only, keep current color scheme but add in some splash of color from the logo
Should not have
• animated characters or cartoon drawings

```html
<!DOCTYPE html>
<html lang="en">
<head>
<meta charset="utf-8">
<title>Quorvane — Technology For Healthcare</title>
<link href="https://fonts.googleapis.com/css2?family=Poppins:wght@400;500;600;700;800&display=swap" rel="stylesheet">
<style>
:root{
  --cyan:#1fbad6;
  --cyan-bright:#2cc4dc;
  --navy:#0b1a57;
  --ink:#0e1240;
  --text:#6d7388;
  --line:#d9e4ee;
  --soft:#f5f7fb;
  --white:#ffffff;
  --violet:#7b61ff;
  --amber:#f5a623;
}
*{box-sizing:border-box;margin:0;padding:0}
html,body{width:1200px;height:5335px;overflow:hidden}
body{position:relative;font-family:'Poppins',sans-serif;color:var(--ink);background:var(--white)}
.abs{position:absolute}
.btn{position:absolute;display:flex;align-items:center;justify-content:center;background:var(--cyan);color:var(--white);font-size:11px;font-weight:500;border-radius:0 0 14px 0}
.h-big{font-weight:800;font-size:48px;line-height:56px;color:var(--ink)}
.eyebrow{font-size:12px;font-weight:500;color:var(--navy)}
.para{font-size:11px;line-height:19px;color:var(--text)}
/* hero */
.hero{position:absolute;left:0;top:0;width:1200px;height:591px;background:linear-gradient(120deg,#0a2c70 0%,#1b58a8 55%,#2a79c8 100%)}
.logo{position:absolute;display:flex;align-items:center;gap:8px;font-weight:700;font-size:20px;letter-spacing:1px}
.logo i{display:block;width:16px;height:16px;background:var(--cyan);border-radius:3px}
.nav{position:absolute;left:580px;top:29px;display:flex;gap:18px;font-size:11px;font-weight:500;color:var(--white)}
.nav .on{color:var(--cyan-bright)}
.hero h1{position:absolute;left:151px;top:192px;font-size:56px;line-height:60px;font-weight:800;color:var(--white)}
.play{position:absolute;left:801px;top:294px;width:60px;height:60px;border-radius:50%;background:var(--white);box-shadow:0 0 0 8px rgba(255,255,255,.25);display:flex;align-items:center;justify-content:center}
/* services */
.services{position:absolute;left:151px;top:564px;width:898px;height:199px;background:var(--white);border-radius:0 0 40px 0;box-shadow:0 10px 30px rgba(10,30,80,.08);display:flex}
.svc{flex:1;text-align:center;border-right:1px solid var(--line);padding-top:26px}
.svc:last-child{border-right:none}
.svc h4{font-size:14px;font-weight:600;margin:12px 0 10px}
.svc p{font-size:10px;line-height:17px;color:var(--text);width:160px;margin:0 auto}
.svc .arr{width:22px;height:20px;border:1px solid var(--cyan);border-radius:3px;margin:14px auto 0;display:flex;align-items:center;justify-content:center}
/* markets */
.markets{position:absolute;left:0;top:1426px;width:1200px;height:834px;background:var(--soft)}
.mcard{position:absolute;width:283px;height:254px;background:var(--white);border:1px solid var(--cyan);border-radius:0 0 30px 0;padding:26px 30px}
.mcard h4{font-size:16px;font-weight:500;margin:14px 0 14px}
.mcard p{font-size:10.5px;line-height:18.5px;color:var(--text)}
.mcard.fill{background:var(--cyan);color:var(--white)}
.mcard.fill p{color:#e7fbff}
/* cta */
.cta{position:absolute;left:0;top:2260px;width:1200px;height:439px;background:var(--cyan-bright);text-align:center;color:var(--white)}
.cta h2{font-size:44px;line-height:56px;font-weight:800;margin-top:10px}
/* features */
.chip{position:absolute;border-radius:4px}
/* stories */
.story{position:absolute;top:4291px;width:283px;background:var(--white);box-shadow:0 10px 30px rgba(10,30,80,.1)}
.story .ph{height:212px}
.story h4{font-size:16px;font-weight:600;line-height:24px;margin:34px 24px 0}
.story p{font-size:10px;color:var(--text);margin:20px 24px 0}
.story .btn{position:relative;width:124px;height:43px;margin:22px 24px 38px}
/* footer */
.footer{position:absolute;left:0;top:4965px;width:1200px;height:370px;background:var(--navy);color:var(--white)}
.fcol{position:absolute;top:140px;font-size:10px}
.fcol h5{font-size:15px;font-weight:600;margin-bottom:18px}
.fcol li{list-style:none;margin-bottom:8px;color:#d8def5}
.fcol li::before{content:"›";margin-right:8px;color:var(--white)}
</style>
</head>
<body>

<!-- HERO -->
<section class="hero" role="img" aria-label="Photo of a gloved hand touching a transparent screen of medical scans">
  <div class="logo" style="left:155px;top:22px;color:var(--white)"><i></i>QUORVANE</div>
  <nav class="nav"><span class="on">Home</span><span>About</span><span>Services</span><span>Projects</span><span>Contact</span></nav>
  <div class="btn" style="left:890px;top:22px;width:103px;height:30px;border-radius:2px;font-size:10px">Get A Quote</div>
  <svg class="abs" style="left:1020px;top:28px" width="16" height="16" viewBox="0 0 16 16"><circle cx="6.5" cy="6.5" r="5" fill="none" stroke="#fff" stroke-width="2"/><line x1="10.5" y1="10.5" x2="15" y2="15" stroke="#fff" stroke-width="2"/></svg>
  <h1>Technology For<br>Healthcare</h1>
  <p class="abs" style="left:151px;top:346px;font-size:12px;line-height:20px;color:#e3ecff;width:470px">Lorem ipsum dolor sit amet, consectetur adipiscing elit. Ut elit tellus, luctus nec ullamcorper mattis, pulvinar dapibus leo.</p>
  <div class="btn" style="left:151px;top:415px;width:124px;height:42px">Get Started</div>
  <div class="play"><svg width="18" height="20" viewBox="0 0 18 20"><path d="M2 1l15 9-15 9z" fill="#2a79c8"/></svg></div>
</section>

<!-- SERVICES -->
<section class="services">
  <div class="svc">
    <svg width="32" height="30" viewBox="0 0 32 30" fill="none" stroke="#1fbad6" stroke-width="1.6"><rect x="2" y="2" width="28" height="19" rx="2"/><path d="M10 28h12M16 21v7M9 14l4-5 4 3 6-6"/></svg>
    <h4>Teleradiology</h4><p>End to End workflow to and from anywhere</p>
    <div class="arr"><svg width="8" height="10" viewBox="0 0 8 10"><path d="M2 1l4 4-4 4" stroke="#0e1240" fill="none" stroke-width="1.5"/></svg></div>
  </div>
  <div class="svc">
    <svg width="32" height="30" viewBox="0 0 32 30" fill="none" stroke="#1fbad6" stroke-width="1.6"><rect x="4" y="7" width="24" height="19" rx="3"/><path d="M12 7V3h8v4M16 12v9M11.5 16.5h9"/></svg>
    <h4>Clinical</h4><p>Highly Subspecialized Clinicians</p>
    <div class="arr"><svg width="8" height="10" viewBox="0 0 8 10"><path d="M2 1l4 4-4 4" stroke="#0e1240" fill="none" stroke-width="1.5"/></svg></div>
  </div>
  <div class="svc">
    <svg width="32" height="30" viewBox="0 0 32 30" fill="none" stroke="#1fbad6" stroke-width="1.6"><rect x="6" y="2" width="20" height="26" rx="2"/><path d="M11 9h10M11 14h10M11 19h6"/><path d="M19 21l2 2 4-4"/></svg>
    <h4>Compliance</h4><p>Integrated compliance across various verticals</p>
    <div class="arr"><svg width="8" height="10" viewBox="0 0 8 10"><path d="M2 1l4 4-4 4" stroke="#0e1240" fill="none" stroke-width="1.5"/></svg></div>
  </div>
  <div class="svc">
    <svg width="32" height="30" viewBox="0 0 32 30" fill="none" stroke="#1fbad6" stroke-width="1.6"><path d="M5 4l22 22M27 4L5 26"/><circle cx="6" cy="5" r="3"/><circle cx="26" cy="5" r="3"/><rect x="12" y="12" width="8" height="6" rx="1"/></svg>
    <h4>PACS/RIS</h4><p>Affordable PACS/RIS replacement</p>
    <div class="arr"><svg width="8" height="10" viewBox="0 0 8 10"><path d="M2 1l4 4-4 4" stroke="#0e1240" fill="none" stroke-width="1.5"/></svg></div>
  </div>
</section>

<!-- ABOUT -->
<section>
  <p class="eyebrow abs" style="left:151px;top:818px">About Us</p>
  <h2 class="h-big abs" style="left:151px;top:850px">Purpose built<br>Technology</h2>
  <p class="para abs" style="left:151px;top:993px;width:430px">Our end to end workflow platform is purposely built for remote access from anywhere in the world while providing centralized management access.</p>
  <svg class="abs" style="left:153px;top:1058px" width="32" height="32" viewBox="0 0 32 32" fill="none" stroke="#1fbad6" stroke-width="1.6"><circle cx="16" cy="16" r="11"/><circle cx="16" cy="16" r="5"/><path d="M3 3l6 6M29 3l-6 6M3 29l6-6M29 29l-6-6"/></svg>
  <h4 class="abs" style="left:213px;top:1064px;font-size:14px;font-weight:600">Our Mission &amp; Vission</h4>
  <p class="para abs" style="left:213px;top:1092px;width:345px">Lorem ipsum dolor sit amet, consectetur adipiscing elit, sed do eiusmod tempor incididunt ut labore et dolore magna aliqua. Ut enim ad minim veniam, quis nostrud exercitation.</p>
  <svg class="abs" style="left:151px;top:1180px" width="38" height="38" viewBox="0 0 38 38" fill="none" stroke="#1fbad6" stroke-width="1.6"><path d="M14 24c4-12 12-18 21-21-3 9-9 17-21 21z"/><circle cx="26" cy="12" r="3"/><path d="M14 24l-4-4 6-4M14 24l4 4 4-6M9 29c-3 1-5 4-6 6 2-1 5-3 6-6z"/></svg>
  <h4 class="abs" style="left:213px;top:1188px;font-size:14px;font-weight:600">Our Approach</h4>
  <p class="para abs" style="left:213px;top:1216px;width:345px">Lorem ipsum dolor sit amet, consectetur adipiscing elit, sed do eiusmod tempor incididunt ut labore et dolore magna aliqua. Ut enim ad minim veniam, quis nostrud exercitation.</p>
  <div class="btn" style="left:151px;top:1307px;width:124px;height:42px">Get Started</div>
  <div class="abs" role="img" aria-label="Photo of clinicians reviewing scans on a laptop" style="left:808px;top:852px;width:241px;height:218px;border-radius:0 50px 0 0;background:linear-gradient(135deg,#3c5f86,#8fb4d3 60%,#d6e2ee)"></div>
  <div class="abs" role="img" aria-label="Photo of a smiling medical team in white coats" style="left:643px;top:1067px;width:406px;height:233px;border-radius:0 0 40px 0;background:linear-gradient(135deg,#2a2f3a,#7f8794 50%,#c9a98a)"></div>
  <div class="abs" style="left:684px;top:868px;width:124px;height:126px;background:var(--cyan);color:#fff;text-align:center;border-radius:0 0 24px 0">
    <div style="font-size:44px;font-weight:600;margin-top:18px;line-height:50px">19</div>
    <div style="font-size:11px;font-weight:500;margin-top:10px">Year Experience</div>
  </div>
</section>

<!-- MARKETS -->
<section class="markets">
  <p class="eyebrow abs" style="left:151px;top:108px;font-size:11px">Adaptive Solutions for every Market</p>
  <h2 class="h-big abs" style="left:151px;top:133px">Markets</h2>
  <div class="mcard fill" style="left:151px;top:228px">
    <svg width="26" height="28" viewBox="0 0 26 28" fill="none" stroke="#fff" stroke-width="1.6"><rect x="3" y="2" width="20" height="24" rx="1"/><path d="M13 6v6M10 9h6M8 16h3M15 16h3M8 21h3M15 21h3"/></svg>
    <h4>Hospitals</h4><p>Lorem ipsum dolor sit amet, consecte tur adipisicing elit, sed do eiusmod tempor incididunt ut labore et dolore magna aliqua. Ut enim ad minim veniam, quis nostrud exercitation.</p>
  </div>
  <div class="mcard" style="left:151px;top:514px">
    <svg width="32" height="28" viewBox="0 0 32 28" fill="none" stroke="#1fbad6" stroke-width="1.6"><circle cx="9" cy="7" r="3"/><circle cx="16" cy="4" r="3"/><circle cx="23" cy="7" r="3"/><circle cx="5" cy="14" r="3"/><circle cx="27" cy="14" r="3"/><path d="M10 24c0-6 3-10 6-10s6 4 6 10c-4 2-8 2-12 0z"/></svg>
    <h4>Veterinarian</h4><p>Lorem ipsum dolor sit amet, consecte tur adipisicing elit, sed do eiusmod tempor incididunt ut labore et dolore magna aliqua. Ut enim ad minim veniam, quis nostrud exercitation.</p>
  </div>
  <div class="mcard" style="left:458px;top:110px">
    <svg width="32" height="28" viewBox="0 0 32 28" fill="none" stroke="#1fbad6" stroke-width="1.6"><path d="M16 12c-3-3-7-5-7-8a3 3 0 016-1 3 3 0 016 1c0 3-3 5-5 8z"/><path d="M3 20l6-3h8a2 2 0 010 4h-6M3 26l5-3h12l8-7"/></svg>
    <h4>Urgent Care</h4><p>Lorem ipsum dolor sit amet, consecte tur adipisicing elit, sed do eiusmod tempor incididunt ut labore et dolore magna aliqua. Ut enim ad minim veniam, quis nostrud exercitation.</p>
  </div>
  <div class="mcard" style="left:458px;top:396px">
    <svg width="32" height="30" viewBox="0 0 32 30" fill="none" stroke="#1fbad6" stroke-width="1.6"><rect x="2" y="2" width="28" height="20" rx="1"/><path d="M10 28h12M16 22v6M7 8h8M7 13h8M19 7h6v9h-6z"/></svg>
    <h4>Acute Care</h4><p>Lorem ipsum dolor sit amet, consecte tur adipisicing elit, sed do eiusmod tempor incididunt ut labore et dolore magna aliqua. Ut enim ad minim veniam, quis nostrud exercitation.</p>
  </div>
  <div class="mcard" style="left:766px;top:228px">
    <svg width="28" height="28" viewBox="0 0 28 28" fill="none" stroke="#1fbad6" stroke-width="1.6"><rect x="3" y="2" width="22" height="24" rx="1"/><path d="M8 7h3M13 7h3M18 7h2M8 12h3M13 12h3M18 12h2M8 17h3M13 17h3M18 17h2M12 26v-4h4v4"/></svg>
    <h4>Government Health</h4><p>Lorem ipsum dolor sit amet, consecte tur adipisicing elit, sed do eiusmod tempor incididunt ut labore et dolore magna aliqua. Ut enim ad minim veniam, quis nostrud exercitation.</p>
  </div>
  <div class="btn" style="left:766px;top:514px;width:164px;height:42px">Find Your Solution</div>
</section>

<!-- CTA -->
<section class="cta" role="region" aria-label="Call to action">
  <div class="abs" role="img" aria-label="Faint dotted world map" style="left:300px;top:40px;width:700px;height:360px;background:radial-gradient(ellipse at center,rgba(255,255,255,.12),rgba(255,255,255,0) 70%)"></div>
  <p style="font-size:11px;color:var(--navy);margin-top:76px;position:relative">Give Us A Call</p>
  <h2 style="position:relative">Are You Ready to<br>Accelerate Your<br>Business?</h2>
  <div class="abs" style="left:420px;top:308px;width:360px;height:50px;display:flex;border-radius:0 0 18px 0;overflow:hidden">
    <div style="flex:1;border:2px solid #fff;border-right:none;display:flex;align-items:center;justify-content:center;font-size:11px;font-weight:500;border-radius:18px 0 0 0">Join Today</div>
    <div style="flex:1;background:var(--navy);display:flex;align-items:center;justify-content:center;font-size:11px;font-weight:500">Contact Us</div>
  </div>
  <div class="abs" style="left:584px;top:317px;width:32px;height:32px;border-radius:50%;background:#fff;color:var(--ink);font-size:10px;font-weight:600;display:flex;align-items:center;justify-content:center;box-shadow:0 0 0 4px rgba(255,255,255,.3)">Or</div>
</section>

<!-- FEATURE: GRC -->
<section>
  <h2 class="h-big abs" style="left:151px;top:2893px">All-in-one GRC<br>platform</h2>
  <p class="para abs" style="left:151px;top:3021px;width:410px">Provide Users With Appropriate View And Access Permissions To Requests, Problems, Changes, Contracts, Assets, Solutions, And Reports With Our Experienced Professionals.</p>
  <div class="btn" style="left:151px;top:3111px;width:170px;height:44px">Pricing &amp; Plans</div>
  <div class="abs" style="left:593px;top:2869px;width:431px;height:286px;background:#fff;box-shadow:0 10px 30px rgba(10,30,80,.1);border-radius:8px 0 0 8px;overflow:hidden">
    <div class="abs" style="left:0;top:0;width:28px;height:286px;background:var(--violet)"></div>
    <div class="chip" style="left:42px;top:48px;width:80px;height:26px;background:#fff;box-shadow:0 2px 8px rgba(0,0,0,.08)"></div>
    <div class="chip" style="left:132px;top:48px;width:80px;height:26px;background:#fff;box-shadow:0 2px 8px rgba(0,0,0,.08)"></div>
    <div class="chip" style="left:222px;top:48px;width:80px;height:26px;background:var(--violet)"></div>
    <svg class="abs" style="left:312px;top:48px" width="70" height="26"><path d="M2 20l12-8 10 6 12-12 12 10 12-6" fill="none" stroke="#ff8aa6" stroke-width="2"/></svg>
    <svg class="abs" style="left:42px;top:98px" width="200" height="80"><g fill="#0e1240"><rect x="10" y="40" width="4" height="36"/><rect x="40" y="20" width="4" height="56"/><rect x="70" y="30" width="4" height="46"/><rect x="100" y="10" width="4" height="66"/><rect x="130" y="35" width="4" height="41"/><rect x="160" y="15" width="4" height="61"/></g><g fill="#22c55e"><rect x="16" y="55" width="4" height="21"/><rect x="76" y="50" width="4" height="26"/><rect x="136" y="55" width="4" height="21"/></g></svg>
    <div class="chip" style="left:320px;top:98px;width:100px;height:170px;background:#f3f1ff"></div>
    <svg class="abs" style="left:42px;top:200px" width="110" height="60"><path d="M2 50l14-20 14 10 16-28 16 24 16-14 20 6" fill="none" stroke="#ef4444" stroke-width="1.6"/></svg>
    <div class="chip" style="left:170px;top:200px;width:130px;height:70px;background:#fafbff;border:1px solid #eee"></div>
  </div>
</section>

<!-- FEATURE: RISK -->
<section>
  <div class="abs" style="left:185px;top:3362px;font-size:11px;font-weight:600;color:#333">Top Graphic</div>
  <div class="abs" style="left:316px;top:3343px;width:234px;height:52px;background:var(--violet);border-radius:6px;color:#fff;display:flex;align-items:center;gap:10px;padding-left:16px;font-size:14px">
    <svg width="22" height="22" viewBox="0 0 22 22"><circle cx="11" cy="11" r="9" fill="none" stroke="#fff" stroke-width="1.6"/><path d="M7 11l3 3 5-6" fill="none" stroke="#fff" stroke-width="1.6"/></svg>Privacy Software
  </div>
  <svg class="abs" style="left:185px;top:3410px" width="330" height="180" viewBox="0 0 330 180">
    <g font-size="10" fill="#555" font-family="Poppins,sans-serif"><text x="6" y="12">40</text><text x="6" y="48">30</text><text x="6" y="84">20</text><text x="6" y="120">10</text><text x="10" y="156">0</text></g>
    <g fill="#0e1240"><rect x="46" y="118" width="6" height="36"/><rect x="110" y="36" width="6" height="118"/><rect x="174" y="92" width="6" height="62"/><rect x="238" y="60" width="6" height="94"/></g>
    <g fill="#e4e6ee"><rect x="56" y="98" width="6" height="56"/><rect x="120" y="78" width="6" height="76"/><rect x="184" y="104" width="6" height="50"/><rect x="248" y="118" width="6" height="36"/></g>
    <g fill="#6b5cff"><rect x="178" y="58" width="6" height="96"/><rect x="300" y="86" width="6" height="68"/></g>
    <rect x="290" y="14" width="6" height="140" fill="#f5a623"/>
  </svg>
  <h2 class="h-big abs" style="left:623px;top:3313px">Real-time risk<br>monitoring</h2>
  <p class="para abs" style="left:623px;top:3438px;width:410px">Provide Users With Appropriate View And Access Permissions To Requests, Problems, Changes, Contracts, Assets, Solutions, And Reports With Our Experienced Professionals.</p>
  <div class="btn" style="left:623px;top:3540px;width:162px;height:42px">Pricing &amp; Plans</div>
</section>

<!-- FEATURE: COLLAB -->
<section>
  <h2 class="h-big abs" style="left:151px;top:3729px">Collaborative<br>workflows</h2>
  <p class="para abs" style="left:151px;top:3855px;width:410px">Provide Users With Appropriate View And Access Permissions To Requests, Problems, Changes, Contracts, Assets, Solutions, And Reports With Our Experienced Professionals.</p>
  <div class="btn" style="left:151px;top:3945px;width:170px;height:44px">Pricing &amp; Plans</div>
  <div class="abs" style="left:591px;top:3725px;width:449px;height:320px;background:#fff;box-shadow:0 10px 30px rgba(10,30,80,.1)">
    <div class="abs" style="left:0;top:0;width:180px;height:320px;background:#1f2330"></div>
    <div class="abs" style="left:0;top:0;width:24px;height:320px;background:#171a24"></div>
    <div class="abs" style="left:36px;top:36px;width:132px;height:28px;background:#2a2f3e;border-radius:3px"></div>
    <div class="abs" style="left:36px;top:76px;width:132px;height:28px;background:#2a2f3e;border-radius:3px"></div>
    <div class="abs" style="left:36px;top:116px;width:132px;height:28px;background:#2a2f3e;border-radius:3px"></div>
    <div class="abs" style="left:36px;top:156px;width:132px;height:28px;background:#2a2f3e;border-radius:3px"></div>
    <div class="abs" style="left:36px;top:196px;width:132px;height:28px;background:#2a2f3e;border-radius:3px"></div>
    <div class="abs" style="left:195px;top:20px;font-size:8px;color:#444">Mara Quillen</div>
    <div class="abs" style="left:220px;top:60px;width:150px;height:34px;background:#f1f2f6;border-radius:4px"></div>
    <div class="abs" style="left:220px;top:110px;width:150px;height:40px;background:#f1f2f6;border-radius:4px"></div>
    <div class="abs" style="left:220px;top:165px;width:180px;height:52px;background:#4f46e5;border-radius:4px"></div>
    <div class="abs" style="left:220px;top:230px;width:180px;height:32px;background:#4f46e5;border-radius:4px"></div>
    <div class="abs" style="left:190px;top:290px;width:250px;height:1px;background:#e5e7eb"></div>
  </div>
</section>

<!-- SUCCESS STORIES -->
<section>
  <p class="eyebrow abs" style="left:0;width:1200px;text-align:center;top:4164px;font-size:11px">Latest Case Studies</p>
  <h2 class="h-big abs" style="left:0;width:1200px;text-align:center;top:4196px;font-size:46px">Success Stories</h2>
  <article class="story" style="left:151px">
    <div class="ph" role="img" aria-label="Photo of a modern office tower at dusk" style="background:linear-gradient(180deg,#2c3a86,#5e6fb8 60%,#c9b28a)"></div>
    <h4>Retrofit Submetering With Next-gen Tech</h4><p>Retrofit Submetering With Next-gen Tech</p>
    <div class="btn">Learn more</div>
  </article>
  <article class="story" style="left:458px">
    <div class="ph" role="img" aria-label="Photo looking up at glass skyscrapers" style="background:linear-gradient(160deg,#1f2a36,#5a6d80 55%,#aab9c8)"></div>
    <h4>Auxiliary Submetering for HVAC Equipmen</h4><p>Auxiliary Submetering for HVAC Equipmen</p>
    <div class="btn">Learn more</div>
  </article>
  <article class="story" style="left:766px">
    <div class="ph" role="img" aria-label="Photo of city office buildings under a blue sky" style="background:linear-gradient(180deg,#3c5fae,#7f9ccb 55%,#4d5566)"></div>
    <h4>Water Metering Retrofit</h4><p>Water Metering Retrofit</p>
    <div class="btn">Learn more</div>
  </article>
</section>

<!-- FOOTER -->
<footer class="footer">
  <div class="abs" style="left:187px;top:-143px;width:825px;height:215px;background:var(--cyan);border-radius:70px 0 70px 0">
    <p class="abs" style="left:78px;top:52px;font-size:11px;color:var(--navy)">Get Latest Updates</p>
    <h3 class="abs" style="left:78px;top:80px;font-size:28px;line-height:35px;font-weight:800;color:#fff">Subscribe to Our<br>Newsletter</h3>
    <div class="abs" style="left:496px;top:86px;width:229px;height:42px;background:#fff;display:flex;align-items:center;justify-content:center;font-size:9px;color:var(--cyan);letter-spacing:1px">SUBSCRIBE NOW ›</div>
  </div>
  <div class="logo" style="left:151px;top:138px;color:#fff"><i></i>QUORVANE</div>
  <p class="abs" style="left:151px;top:183px;width:270px;font-size:10px;line-height:16px;color:#d8def5">Quis ipsum suspendisse ultrices lorem gravida. Risus commodo viverra maecenas accumsan.</p>
  <div class="abs" style="left:151px;top:242px;display:flex;gap:10px">
    <i style="width:22px;height:22px;background:var(--cyan);border-radius:3px"></i><i style="width:22px;height:22px;background:var(--cyan);border-radius:3px"></i><i style="width:22px;height:22px;background:var(--cyan);border-radius:3px"></i><i style="width:22px;height:22px;background:var(--cyan);border-radius:3px"></i>
  </div>
  <div class="fcol" style="left:516px"><h5>Services</h5><ul><li>StreamlineThe Trial</li><li>Constan Innovation</li><li>Cloud Based Data Storage</li><li>CTMS Platform</li><li>Integrated User Platform</li><li>18/6 Support</li></ul></div>
  <div class="fcol" style="left:752px"><h5>Quick Links</h5><ul><li>About Us</li><li>Services</li><li>Pricing</li><li>Blog</li><li>Contact</li></ul></div>
  <div class="fcol" style="left:932px"><h5>Contact</h5>
    <p style="color:#d8def5;margin-bottom:8px">⌖ &nbsp;Harbor District</p>
    <p style="color:#d8def5;margin-bottom:8px">✉ &nbsp;mail@quorvane.com</p>
    <p style="color:#d8def5">☎ &nbsp;+62-000-555-0</p>
  </div>
  <div class="abs" style="left:151px;top:335px;width:898px;height:1px;background:rgba(255,255,255,.15)"></div>
  <p class="abs" style="left:151px;top:350px;font-size:9px;color:#d8def5">Copyright © 2025 Quorvane. All Rights Reserved.</p>
  <p class="abs" style="left:874px;top:350px;font-size:9px;color:#d8def5">Privacy Policy &nbsp;&nbsp; Terms &amp; Conditions</p>
</footer>

</body>
</html>
```